Attractive door board for entrance beautysalon

Make an attractive design for a board that can be glued on the front door of a beauty salon. The salon location has no window in the front so I need something catchy and attractive. The door board contains a list of the services and the website: www.velmora.be, and the text "Enkel op afspraak, bel 0486319542"

Target Market(s)

woman between 16 and 99 years old

Industry/Entity Type

Beauty Salon

Font styles to use
Sans Serif

Requirements
Must have
• A very nice, attractive but sober design.
• It must have a classy Marvaux, Quen, ... chique design.
• The logo must be on it (in attachment)
• There must be the following list in it:
• Gelaatsverzorging
• Wimperverlenging
• Wimperlifting
• Suikerontharing
• Permanente Make Up
• Airbrush Tanning
• Manicure - Pedicure - Tovira
• and then the website www.velmora.be, and the text "Enkel op afspraak, bel 0486319542"
Nice to have
• a catchy design,
• max. width can be 75 cm and max height 180 cm as it is a design for a board that will be glued on a door.
Should not have
• orchid flowers, buddha look a likes

```html
<!DOCTYPE html>
<html lang="nl">
<head>
<meta charset="utf-8">
<title>Velmora – deurbord varianten</title>
<link rel="stylesheet" href="https://fonts.googleapis.com/css2?family=Lato:wght@400;700;900&display=swap">
<style>
  :root {
    --page: #f8f8f8;
    --ink: #000000;
    --paper: #ffffff;
    --frame-on-dark: #9a9a9a;
    --frame-on-light: #777777;
  }
  * { margin: 0; padding: 0; box-sizing: border-box; }
  html, body {
    width: 1200px; height: 1200px; overflow: hidden;
    background: var(--page);
    font-family: "Lato", Arial, sans-serif;
  }
  .board {
    position: absolute; top: 234px;
    width: 305px; height: 732px;
  }
  .board--dark { background: var(--ink); color: var(--paper); }
  .board--light { background: var(--paper); color: var(--ink); box-shadow: 0 0 0 1px #e6e6e6; }
  .board--one { left: 89px; }
  .board--two { left: 447px; }
  .board--three { left: 806px; }

  .plate {
    position: absolute; left: 51px; top: 35px;
    width: 202px; height: 299px;
    text-align: center;
  }
  .board--dark .plate--framed { border: 1px solid var(--frame-on-dark); }
  .board--light .plate--framed { border: 1px solid var(--frame-on-light); }

  .plate > * { position: absolute; left: 0; right: 0; }

  .mark {
    top: 28px; margin: 0 auto;
    width: 30px; height: 30px;
    border: 1.5px solid currentColor; border-radius: 50%;
  }
  .brand-name {
    top: 82px; font-size: 14px; font-weight: 400;
    letter-spacing: 0.62em; padding-left: 0.62em;
  }
  .brand-tagline {
    top: 106px; font-size: 5px; font-weight: 900;
    letter-spacing: 0.72em; padding-left: 0.72em;
  }
  .rule {
    left: 23px; right: 23px; height: 2px;
    background: currentColor;
  }
  .rule--top { top: 130px; }
  .rule--bottom { top: 236px; }

  .services {
    top: 148px; list-style: none;
    font-size: 5.6px; font-weight: 700;
    letter-spacing: 0.16em; line-height: 11.2px;
    text-transform: uppercase;
  }
  .website {
    top: 251px; font-size: 10px; font-weight: 700;
    letter-spacing: 0.42em; padding-left: 0.42em;
  }
  .booking {
    top: 271px; font-size: 6px; font-weight: 700;
    letter-spacing: 0.14em; text-transform: uppercase;
  }
  .booking .phone { font-size: 7.5px; letter-spacing: 0.12em; }
</style>
</head>
<body>

<section class="board board--dark board--one">
  <div class="plate plate--framed">
    <div class="mark"></div>
    <div class="brand-name">VELMORA</div>
    <div class="brand-tagline">SCHOONHEIDSINSTITUUT</div>
    <div class="rule rule--top"></div>
    <ul class="services">
      <li>Gelaatsverzorging</li>
      <li>Wimperverlenging</li>
      <li>Wimperlifting</li>
      <li>Suikerontharing</li>
      <li>Permanente make up</li>
      <li>Airbrush tanning</li>
      <li>Manicure - Pedicure - Tovira</li>
    </ul>
    <div class="rule rule--bottom"></div>
    <div class="website">www.velmora.be</div>
    <div class="booking">Enkel op afspraak, bel <span class="phone">0486319542</span></div>
  </div>
</section>

<section class="board board--dark board--two">
  <div class="plate">
    <div class="mark"></div>
    <div class="brand-name">VELMORA</div>
    <div class="brand-tagline">SCHOONHEIDSINSTITUUT</div>
    <div class="rule rule--top"></div>
    <ul class="services">
      <li>Gelaatsverzorging</li>
      <li>Wimperverlenging</li>
      <li>Wimperlifting</li>
      <li>Suikerontharing</li>
      <li>Permanente make up</li>
      <li>Airbrush tanning</li>
      <li>Manicure - Pedicure - Tovira</li>
    </ul>
    <div class="rule rule--bottom"></div>
    <div class="website">www.velmora.be</div>
    <div class="booking">Enkel op afspraak, bel <span class="phone">0486319542</span></div>
  </div>
</section>

<section class="board board--light board--three">
  <div class="plate plate--framed">
    <div class="mark"></div>
    <div class="brand-name">VELMORA</div>
    <div class="brand-tagline">SCHOONHEIDSINSTITUUT</div>
    <div class="rule rule--top"></div>
    <ul class="services">
      <li>Gelaatsverzorging</li>
      <li>Wimperverlenging</li>
      <li>Wimperlifting</li>
      <li>Suikerontharing</li>
      <li>Permanente make up</li>
      <li>Airbrush tanning</li>
      <li>Manicure - Pedicure - Tovira</li>
    </ul>
    <div class="rule rule--bottom"></div>
    <div class="website">www.velmora.be</div>
    <div class="booking">Enkel op afspraak, bel <span class="phone">0486319542</span></div>
  </div>
</section>

</body>
</html>
```